Site for a workout and Consulting enterprise

I need a professional responsive site for www.valomer.hamburg. The website shoulderstand consist of a Landing and 4 other pages. - On page for the contact informations - on page for the about - on page for consulting services (technical) - on page for Training and workshop services (business and soft skills) I add some files so you can see my idea of the design.
Target Market(s)
IT and Management
Industry/Entity Type
Management Consulting
Coding
Coded - Design and coding required
Number of Pages Required
4 page
Requirements
Must have
- Use Pictures for Background, Sliders and Topics. Just have to placeholders for the design.

```html
<!DOCTYPE html>
<html lang="de">
<head>
<meta charset="utf-8">
<title>Valomer – Individuen, Ideen, Innovationen</title>
<link rel="stylesheet" href="https://fonts.googleapis.com/css2?family=Roboto:wght@300;400;500;700&display=swap">
<style>
  :root {
    --photo-dark: #2e2a22;
    --photo-mid: #5a4c38;
    --photo-warm: #7a5a3a;
    --photo-green: #4d5a36;
    --panel: rgba(235, 235, 230, 0.22);
    --white: #ffffff;
    --text-soft: rgba(255, 255, 255, 0.9);
    --teal: #0f9a86;
    --green: #43b049;
    --cyan: #00b6d2;
    --accent-blue: #3b4fcf;
    --link: #cddc2a;
  }
  * { box-sizing: border-box; margin: 0; padding: 0; }
  html, body { width: 1200px; height: 675px; overflow: hidden; }
  body { font-family: "Roboto", Arial, sans-serif; color: var(--white); }

  .landing { position: relative; width: 1200px; height: 675px; overflow: hidden; }

  .hero-photo {
    position: absolute; inset: 0;
    background:
      radial-gradient(ellipse 40% 30% at 70% 12%, rgba(190, 200, 180, 0.55), transparent 70%),
      radial-gradient(ellipse 60% 40% at 30% 85%, rgba(120, 110, 95, 0.6), transparent 70%),
      linear-gradient(180deg, var(--photo-green) 0%, var(--photo-warm) 38%, var(--photo-mid) 65%, var(--photo-dark) 100%);
  }

  .brand { position: absolute; left: 106px; top: 262px; }
  .brand-name {
    font-weight: 400; font-size: 104px; line-height: 1; letter-spacing: 1px;
    color: var(--white);
  }
  .brand-tagline { margin-top: 14px; font-weight: 400; font-size: 24.5px; color: var(--white); }

  .info-panel {
    position: absolute; left: 601px; top: 24px; width: 576px; height: 628px;
    background: var(--panel); overflow: hidden;
  }
  .panel-toggle { position: absolute; left: 0; top: 236px; width: 80px; height: 156px; }

  .topic { position: absolute; display: flex; align-items: center; }
  .topic-badge {
    width: 75px; height: 75px; border-radius: 50%; flex: none;
    display: flex; align-items: center; justify-content: center;
    font-size: 29px; font-weight: 400; color: var(--white);
  }
  .topic-body { margin-left: 22px; }
  .topic-title { font-size: 18px; font-weight: 500; margin-bottom: 7px; }
  .topic-text { font-size: 15.5px; font-weight: 300; line-height: 21px; color: var(--text-soft); }

  .topic-one   { left: 82px;  top: 157px; }
  .topic-two   { left: 132px; top: 277px; }
  .topic-three { left: 82px;  top: 397px; }
  .topic-one .topic-badge   { background: var(--teal); }
  .topic-two .topic-badge   { background: var(--green); }
  .topic-three .topic-badge { background: var(--cyan); }

  .panel-footer {
    position: absolute; left: 0; right: 0; bottom: 18px; text-align: center;
    font-size: 14.5px; color: var(--link); padding-left: 0;
  }
  .panel-footer a { color: var(--link); text-decoration: none; }
  .panel-footer .divider { margin: 0 8px; }
</style>
</head>
<body>
<main class="landing">
  <div class="hero-photo" role="img" aria-label="Hintergrundfoto: alte Bahngleise mit Herbstlaub und einer verrosteten Weichenstellvorrichtung"></div>

  <header class="brand">
    <h1 class="brand-name">Valomer</h1>
    <p class="brand-tagline">Individuen, Ideen, Innovationen</p>
  </header>

  <section class="info-panel">
    <svg class="panel-toggle" viewBox="0 0 80 156" aria-label="Menü öffnen">
      <path d="M0 0 A78 78 0 0 1 0 156 Z" fill="var(--accent-blue)" opacity="0.92"/>
      <path d="M35 78 H65 M50 63 V93" stroke="#fff" stroke-width="2.5" fill="none"/>
    </svg>

    <article class="topic topic-one">
      <div class="topic-badge">1</div>
      <div class="topic-body">
        <h2 class="topic-title">Lorem Ipsum is dummy text</h2>
        <p class="topic-text">Lorem Ipsum is dummy text<br>Lorem Ipsum is dummy text</p>
      </div>
    </article>

    <article class="topic topic-two">
      <div class="topic-badge">2</div>
      <div class="topic-body">
        <h2 class="topic-title">Lorem Ipsum is dummy text</h2>
        <p class="topic-text">Lorem Ipsum is dummy text<br>Lorem Ipsum is dummy text</p>
      </div>
    </article>

    <article class="topic topic-three">
      <div class="topic-badge">3</div>
      <div class="topic-body">
        <h2 class="topic-title">Lorem Ipsum is dummy text</h2>
        <p class="topic-text">Lorem Ipsum is dummy text<br>Lorem Ipsum is dummy text</p>
      </div>
    </article>

    <footer class="panel-footer">
      <a href="#impressum">Impressum</a><span class="divider">|</span><a href="#kontakt">Kontakt</a>
    </footer>
  </section>
</main>
</body>
</html>
```